Book cover design for a book named BLOOM

Hello Designers,
The name of the book is BLOOM and it is about unexpected experiences individuals have which are beyond their control. Occurrences they are unable to overcome or get out of themselves without the help of God. After overcoming these situations they know only God could have done this for them, no one else could have. It is an adult Christian book. I would like you to be as creative as you can with the cover, using color, light, graphic designs, shapes, scale, lines etc. (you are the designers, I don't know how to do these things.) I would like to use the image created on a paperback, hardcover or e book. I tried to use an image from Pixmarble just to give you some idea of my thinking but you do not have to use these hands. The hands should look as if they are giving someone the word TESTIMONY not receiving it. Use of the words provided, the light rays, and some type of hands extended should not change, but how you use them is up to you. Use the words, light rays, and hands however you wish as long as they convey someone giving the word TESTIMONY. The word TESTIMONY should be proportional to the hand in size and should appear as if being held in the actual hand it should not be larger than the book name. It is a Christian book of testimonies. Also for your design samples you can use the name Marlene Quiller for the author. Thank you, please feel free to contact me if you have any questions. I am looking for the cover to be an attention grabber and give the reader something to really think about and remember visually when they see this cover. Thank you again.

Target Market(s)

anyone and christians

Requirements
Must have
• Use of the words provided, the light rays, and some type of hands extended should not change.
Nice to have
• be as creative as you can with the cover, using color, light, graphic designs, shapes, scale, lines etc. (you are the designers, I don't know how to do these things.)
Should not have
• It should not have fonts, colors, etc. that convey it is a child's book, fairytale, or fictional etc. It is a book of true stories that actually happened. It should not look exactly like my example, what I provided.

```html
<!DOCTYPE html>
<html lang="en">
<head>
<meta charset="utf-8">
<title>BLOOM — Marlene Quiller</title>
<link href="https://fonts.googleapis.com/css2?family=Anton&family=Oswald:wght@500;600;700&display=swap" rel="stylesheet">
<style>
  :root {
    --page: #ffffff;
    --cover: #050505;
    --gold-light: #ffe98a;
    --gold-mid: #e8b01c;
    --gold-deep: #8a5a06;
    --red: #e0141c;
    --silver-light: #ffffff;
    --silver-dark: #7d7d7d;
    --glow: #ffffff;
    --warm: #d98a5c;
  }
  html, body {
    margin: 0;
    padding: 0;
    width: 1200px;
    height: 1200px;
    overflow: hidden;
    background: var(--page);
  }
  .book-cover {
    position: absolute;
    left: 238px;
    top: 43px;
    width: 720px;
    height: 1079px;
    display: block;
  }
  .title, .tagline { font-family: "Oswald", "Arial Narrow", sans-serif; font-weight: 700; }
  .offering-text { font-family: "Anton", "Oswald", sans-serif; }
  .author { font-family: "Oswald", "Arial Narrow", sans-serif; font-weight: 600; }
</style>
</head>
<body>
<svg class="book-cover" viewBox="0 0 720 1079" xmlns="http://www.w3.org/2000/svg">
  <defs>
    <linearGradient id="gold" x1="0" y1="0" x2="0" y2="1">
      <stop offset="0" stop-color="var(--gold-light)"/>
      <stop offset="0.45" stop-color="var(--gold-mid)"/>
      <stop offset="0.55" stop-color="var(--gold-deep)"/>
      <stop offset="1" stop-color="var(--gold-light)"/>
    </linearGradient>
    <linearGradient id="silver" x1="0" y1="0" x2="0" y2="1">
      <stop offset="0" stop-color="var(--silver-light)"/>
      <stop offset="0.5" stop-color="var(--silver-light)"/>
      <stop offset="0.6" stop-color="var(--silver-dark)"/>
      <stop offset="1" stop-color="var(--silver-light)"/>
    </linearGradient>
    <linearGradient id="reflection-fade" x1="0" y1="0" x2="0" y2="1">
      <stop offset="0" stop-color="#fff" stop-opacity="0.45"/>
      <stop offset="0.35" stop-color="#fff" stop-opacity="0"/>
    </linearGradient>
    <mask id="reflection-mask" maskContentUnits="userSpaceOnUse">
      <rect x="0" y="312" width="720" height="200" fill="url(#reflection-fade)"/>
    </mask>
    <radialGradient id="light-burst" cx="0.52" cy="0.45" r="0.65">
      <stop offset="0" stop-color="var(--glow)"/>
      <stop offset="0.18" stop-color="#f2f2f2"/>
      <stop offset="0.45" stop-color="#8a8a8a" stop-opacity="0.7"/>
      <stop offset="1" stop-color="var(--cover)" stop-opacity="0"/>
    </radialGradient>
    <radialGradient id="hand-tone" cx="0.5" cy="0.4" r="0.6">
      <stop offset="0" stop-color="#f6c9a8"/>
      <stop offset="0.6" stop-color="var(--warm)"/>
      <stop offset="1" stop-color="#5a2a22" stop-opacity="0"/>
    </radialGradient>
  </defs>

  <rect class="cover-background" width="720" height="1079" fill="var(--cover)"/>

  <g role="img" aria-label="Bright light rays bursting over an open hand held out, offering the word Testimony">
    <rect x="0" y="470" width="720" height="560" fill="url(#light-burst)"/>
    <ellipse cx="360" cy="850" rx="230" ry="95" fill="url(#hand-tone)"/>
  </g>

  <text class="title" x="80" y="312" font-size="300" textLength="562" lengthAdjust="spacingAndGlyphs" fill="url(#gold)">BLOOM</text>
  <g mask="url(#reflection-mask)">
    <text class="title" x="80" y="312" font-size="300" textLength="562" lengthAdjust="spacingAndGlyphs" fill="var(--gold-mid)" transform="translate(0 624) scale(1 -1)">BLOOM</text>
  </g>

  <g class="tagline" fill="url(#gold)" font-size="50" text-anchor="middle">
    <text x="363" y="392" textLength="538" lengthAdjust="spacingAndGlyphs">BEFORE THERE WILL EVER BE A</text>
    <text x="332" y="447">TESTIMONY</text>
    <text x="357" y="502" textLength="520" lengthAdjust="spacingAndGlyphs">THERE MUST ALWAYS BE AN</text>
    <text x="360" y="557">EXPERIENCE</text>
  </g>

  <g class="offering-text" fill="var(--red)" stroke="#ffffff" stroke-width="3" paint-order="stroke" text-anchor="middle">
    <text x="360" y="648" font-size="40" transform="rotate(-6 360 648)">OUT OF THE</text>
    <text x="360" y="712" font-size="40" transform="rotate(-9 360 712)">TEST I'VE GIVEN YOU A</text>
    <text x="372" y="808" font-size="92" transform="rotate(-10 372 808)">TESTIMONY</text>
  </g>

  <text class="author" x="360" y="1022" font-size="74" text-anchor="middle" textLength="540" lengthAdjust="spacingAndGlyphs" fill="url(#silver)">MARLENE QUILLER</text>
</svg>
</body>
</html>
```